New signage for workshop frontage. Tarnell Welding & Repair is the company name. Looking for a cool font, metal fabrication is the trade. Also use TWAR as the logo

```html
<!DOCTYPE html>
<html lang="en">
<head>
<meta charset="utf-8">
<title>Tarnell Welding &amp; Repair – Workshop Frontage Sign</title>
<link rel="stylesheet" href="https://fonts.googleapis.com/css2?family=Anton&family=Poppins:wght@700&display=swap">
<style>
  :root {
    --page-bg: #dadada;
    --sky-blue: #5bc0ff;
    --brand-blue: #0a72bd;
    --ink: #1c1c1c;
    --white: #ffffff;
    --divider: #e2e2e2;
  }
  html, body {
    margin: 0;
    padding: 0;
    width: 1200px;
    height: 1200px;
    overflow: hidden;
    background: var(--page-bg);
  }
  .sign {
    position: absolute;
    left: 20px;
    top: 214px;
    width: 1160px;
    height: 772px;
    display: block;
  }
  .headline { font-family: "Anton", "Impact", sans-serif; }
  .headline--steel { fill: url(#steelText); }
  .headline--blue { fill: var(--sky-blue); }
  .intro { font-family: "Poppins", sans-serif; font-weight: 700; fill: var(--white); }
  .service-label { font-family: "Anton", "Impact", sans-serif; fill: var(--ink); }
  .plate-text { font-family: "Poppins", sans-serif; font-weight: 700; fill: var(--ink); }
  .brand-name { font-family: "Anton", "Impact", sans-serif; fill: var(--ink); }
  .web-address { font-family: "Anton", "Impact", sans-serif; fill: var(--ink); }
  .web-address .domain { fill: var(--brand-blue); }
  .divider { stroke: var(--divider); stroke-width: 2; }
</style>
</head>
<body>
<svg class="sign" viewBox="0 0 1604 1068" xmlns="http://www.w3.org/2000/svg" aria-label="Tarnell Welding and Repair workshop sign">
  <defs>
    <linearGradient id="brushedSteel" x1="0" y1="0" x2="1" y2="0">
      <stop offset="0" stop-color="#262626"/>
      <stop offset="0.12" stop-color="#3a3a3a"/>
      <stop offset="0.2" stop-color="#4a4a4a"/>
      <stop offset="0.32" stop-color="#2b2b2b"/>
      <stop offset="0.5" stop-color="#333333"/>
      <stop offset="0.62" stop-color="#4c4c4c"/>
      <stop offset="0.75" stop-color="#2c2c2c"/>
      <stop offset="1" stop-color="#232323"/>
    </linearGradient>
    <linearGradient id="steelFade" x1="0" y1="0" x2="0" y2="1">
      <stop offset="0" stop-color="#000" stop-opacity="0"/>
      <stop offset="1" stop-color="#000" stop-opacity="0.35"/>
    </linearGradient>
    <linearGradient id="steelText" x1="0" y1="0" x2="1" y2="0">
      <stop offset="0" stop-color="#9c9c9c"/>
      <stop offset="0.2" stop-color="#e8e8e8"/>
      <stop offset="0.35" stop-color="#a8a8a8"/>
      <stop offset="0.55" stop-color="#dcdcdc"/>
      <stop offset="0.75" stop-color="#a0a0a0"/>
      <stop offset="0.88" stop-color="#d2d2d2"/>
      <stop offset="1" stop-color="#8f8f8f"/>
    </linearGradient>
    <linearGradient id="plateSteel" x1="0" y1="0" x2="1" y2="0">
      <stop offset="0" stop-color="#b5b5b5"/>
      <stop offset="0.3" stop-color="#e6e6e6"/>
      <stop offset="0.55" stop-color="#c4c4c4"/>
      <stop offset="0.8" stop-color="#ececec"/>
      <stop offset="1" stop-color="#a9a9a9"/>
    </linearGradient>
  </defs>

  <!-- sign face -->
  <rect class="sign-face" x="0" y="0" width="1604" height="1068" fill="var(--white)"/>
  <g class="steel-panel">
    <path d="M0 0H1604V622H1091V722H0Z" fill="url(#brushedSteel)"/>
    <path d="M0 0H1604V622H1091V722H0Z" fill="url(#steelFade)"/>
  </g>

  <!-- headline -->
  <text class="headline headline--steel" x="109" y="305" font-size="234" textLength="1385" lengthAdjust="spacingAndGlyphs">ENGINEERING &amp;</text>
  <text class="headline headline--blue" x="109" y="534" font-size="234" textLength="1157" lengthAdjust="spacingAndGlyphs">FABRICATION</text>

  <!-- services -->
  <text class="intro" x="111" y="657" font-size="63" textLength="468" lengthAdjust="spacingAndGlyphs">SPECIALISTS IN</text>

  <g class="service-dividers">
    <line class="divider" x1="246" y1="735" x2="246" y2="835"/>
    <line class="divider" x1="548" y1="735" x2="548" y2="835"/>
    <line class="divider" x1="809" y1="735" x2="809" y2="835"/>
  </g>

  <g class="service-ticks">
    <g transform="translate(155 727)">
      <circle r="43" fill="var(--white)"/><circle r="38" fill="#161616"/><circle r="30" fill="var(--brand-blue)"/>
      <path d="M-14 1 L-4 11 L15 -9" fill="none" stroke="var(--white)" stroke-width="8" stroke-linecap="round" stroke-linejoin="round"/>
    </g>
    <g transform="translate(398 727)">
      <circle r="43" fill="var(--white)"/><circle r="38" fill="#161616"/><circle r="30" fill="var(--brand-blue)"/>
      <path d="M-14 1 L-4 11 L15 -9" fill="none" stroke="var(--white)" stroke-width="8" stroke-linecap="round" stroke-linejoin="round"/>
    </g>
    <g transform="translate(676 727)">
      <circle r="43" fill="var(--white)"/><circle r="38" fill="#161616"/><circle r="30" fill="var(--brand-blue)"/>
      <path d="M-14 1 L-4 11 L15 -9" fill="none" stroke="var(--white)" stroke-width="8" stroke-linecap="round" stroke-linejoin="round"/>
    </g>
    <g transform="translate(944 727)">
      <circle r="43" fill="var(--white)"/><circle r="38" fill="#161616"/><circle r="30" fill="var(--brand-blue)"/>
      <path d="M-14 1 L-4 11 L15 -9" fill="none" stroke="var(--white)" stroke-width="8" stroke-linecap="round" stroke-linejoin="round"/>
    </g>
  </g>

  <g class="service-labels">
    <text class="service-label" x="109" y="823" font-size="37" textLength="98" lengthAdjust="spacingAndGlyphs">DESIGN</text>
    <text class="service-label" x="282" y="823" font-size="37" textLength="232" lengthAdjust="spacingAndGlyphs">MANUFACTURING</text>
    <text class="service-label" x="583" y="823" font-size="37" textLength="185" lengthAdjust="spacingAndGlyphs">INSTALLATION</text>
    <text class="service-label" x="847" y="823" font-size="37" textLength="196" lengthAdjust="spacingAndGlyphs">MAINTENANCE</text>
  </g>

  <!-- steel plate -->
  <g class="steel-plate">
    <rect x="1091" y="622" width="513" height="197" fill="#8c8c8c"/>
    <rect x="1097" y="628" width="507" height="185" fill="url(#plateSteel)" stroke="#f4f4f4" stroke-width="2"/>
    <g class="plate-screws" fill="#d8d8d8" stroke="#555" stroke-width="2">
      <g transform="translate(1132 655)"><circle r="8"/><path d="M-4 -4L4 4M4 -4L-4 4"/></g>
      <g transform="translate(1575 655)"><circle r="8"/><path d="M-4 -4L4 4M4 -4L-4 4"/></g>
      <g transform="translate(1132 785)"><circle r="8"/><path d="M-4 -4L4 4M4 -4L-4 4"/></g>
      <g transform="translate(1575 785)"><circle r="8"/><path d="M-4 -4L4 4M4 -4L-4 4"/></g>
    </g>
    <text class="plate-text" x="1159" y="696" font-size="37">OF INDUSTRIAL</text>
    <text class="plate-text" x="1159" y="736" font-size="37">COMMERCIAL</text>
    <text class="plate-text" x="1159" y="776" font-size="37" textLength="355" lengthAdjust="spacingAndGlyphs">INFRASTRUCTURE</text>
  </g>

  <!-- brand and web address -->
  <text class="brand-name" x="109" y="976" font-size="110" textLength="298" lengthAdjust="spacingAndGlyphs">TWAR</text>
  <text class="web-address" x="544" y="974" font-size="49" textLength="967" lengthAdjust="spacing">WWW.<tspan class="domain">TARNELLWELDING</tspan>.NET.AU</text>
</svg>
</body>
</html>
```